Create a professional, fresh and polished oversized post card for law firm specializing in Estate Planning & Probate Law for High Net Worth Clients

Use any picture(s) of your choice (mine or ones you recommend), logo, headshot and company info

www.morvenashcroftlaw.com

Westgate Office - 4100 Birchmont Road, Suite 1500, Charlotte, NC 28214
Kerrington Office - 13480 Oakridge Lane, Suite 300, Charlotte, NC 28269

Phone (704) 555-0187

Use this card for a Free Consultation

Target Market(s)

young and old families too; business owners

Industry/Entity Type

Law Firm

Font styles to use
Serif
Sans Serif

Requirements
Must have
• Use any picture(s) of your choice (mine or ones you recommend), logo, headshot and company info
• www.morvenashcroftlaw.com
• Westgate Office - 4100 Birchmont Road, Suite 1500, Charlotte, NC 28214
• Kerrington Office - 13480 Oakridge Lane, Suite 300, Charlotte, NC 28269
• Phone (704) 555-0187
• Use this card for a Free Consultation
Nice to have
• great colors and great design; like graphics with depth /shading
Should not have
• don't use too many pics - keep it simple

```html
<!DOCTYPE html>
<html lang="en">
<head>
<meta charset="utf-8">
<title>Morven Ashcroft Law – Postcard</title>
<link rel="stylesheet" href="https://fonts.googleapis.com/css2?family=Cinzel:wght@500&family=Courgette&family=Gelasio:wght@400&family=Montserrat:wght@400;700&display=swap">
<style>
  :root{
    --navy:#1f4e79;
    --blue:#1b79a6;
    --blue-dark:#1d5d83;
    --blue-light:#7fb2cf;
    --grey:#8d8f94;
    --ink:#1d1d2b;
    --bg:#f1f1f2;
    --white:#ffffff;
  }
  *{box-sizing:border-box;margin:0;padding:0}
  html,body{width:1200px;height:1000px;overflow:hidden;background:var(--bg)}
  .canvas{position:relative;width:1200px;height:1000px}
  .card{position:absolute;width:622px;height:403px;background:var(--white);overflow:hidden}
  .card svg.art{position:absolute;left:0;top:0}

  /* front */
  .card--front{left:460px;top:82px}
  .photo{position:absolute;right:0;top:0;width:360px;height:403px;
    background:linear-gradient(90deg,rgba(255,255,255,1) 0%,#efe9e1 35%,#d9ccbc 70%,#cbb9a4 100%)}
  .brand{position:absolute;text-align:center;color:var(--navy);font-family:'Gelasio',serif;font-weight:400}
  .brand__mark{width:44px;height:44px;border-radius:50%;background:var(--navy);margin:0 auto 5px}
  .brand__name{font-size:14px;letter-spacing:.5px;line-height:1.1;white-space:nowrap}
  .brand__sub{font-size:8px;letter-spacing:1px}
  .card--front .brand{left:55px;top:16px;width:150px}
  .headline{position:absolute;left:43px;top:170px;font-family:'Gelasio',serif;font-weight:400;font-size:22px;line-height:30px;color:var(--navy)}
  .offer{position:absolute;left:20px;top:302px;color:var(--white);font-family:'Montserrat',sans-serif;font-size:14px;line-height:19px}
  .offer strong{font-weight:700;font-size:14px;letter-spacing:.2px}
  .service{position:absolute;right:66px;top:333px;text-align:center;color:var(--white)}
  .service__title{font-family:'Cinzel',serif;font-size:21px;letter-spacing:.5px}
  .service__url{font-family:'Montserrat',sans-serif;font-size:14px;letter-spacing:.3px}

  /* back */
  .card--back{left:150px;top:514px;width:621px}
  .tagline{position:absolute;left:37px;top:28px;font-family:'Courgette',cursive;font-size:17px;line-height:29px;color:var(--navy);letter-spacing:.4px}
  .headshot{position:absolute;left:38px;top:100px;width:92px;height:102px;background:linear-gradient(160deg,#3b3431,#8a7a62 55%,#d9b99a)}
  .bio{position:absolute;left:145px;top:97px;width:250px;font-family:Arial,Helvetica,sans-serif;color:var(--ink)}
  .bio__name{font-size:12px;font-weight:700;color:var(--ink);margin-bottom:6px}
  .bio__text{font-size:9.3px;line-height:12.4px}
  .signature{position:absolute;left:145px;top:200px;width:140px;height:28px;background:linear-gradient(90deg,rgba(27,121,166,.18),rgba(27,121,166,.05))}
  .card--back .brand{left:30px;top:284px;width:136px}
  .card--back .brand__name{font-size:12px;letter-spacing:.2px}
  .url{position:absolute;left:28px;top:364px;width:140px;text-align:center;white-space:nowrap;font-family:Arial,Helvetica,sans-serif;font-size:9.6px;font-weight:700;color:var(--navy)}
  .offices{position:absolute;left:179px;top:279px;font-family:Arial,Helvetica,sans-serif;font-size:8.6px;line-height:10.6px;color:var(--navy)}
  .office{margin-bottom:6px}
  .office__name{font-weight:700;font-size:9.6px}
  .contact{display:flex;align-items:center;gap:4px;margin-top:2px}
  .contact svg{flex:none}
</style>
</head>
<body>
<main class="canvas">

  <section class="card card--front">
    <div class="photo" role="img" aria-label="Photo of a young child in an aviator cap holding a toy plane in a bright playroom with a world map"></div>
    <svg class="art" width="622" height="403" viewBox="0 0 622 403" aria-hidden="true">
      <defs>
        <linearGradient id="swoosh" x1="0" x2="1">
          <stop offset="0" stop-color="#2f3136"/>
          <stop offset=".5" stop-color="#9a9ca0"/>
          <stop offset="1" stop-color="#d8d9db"/>
        </linearGradient>
      </defs>
      <path d="M0,0 H622 V14 C540,10 440,30 330,72 C230,110 110,108 0,76 Z" fill="#fff"/>
      <path d="M0,76 C110,108 230,110 330,72 C440,30 540,10 622,14" fill="none" stroke="url(#swoosh)" stroke-width="5"/>
      <path d="M0,280 C90,268 200,285 290,320 C400,360 520,320 622,300 V403 H0 Z" fill="#c7dbe6" opacity=".8"/>
      <path d="M0,290 C90,276 190,292 280,328 C360,360 450,345 622,308 V403 H0 Z" fill="var(--blue-light)"/>
      <path d="M0,300 C90,286 190,300 270,338 C330,366 280,403 260,403 H0 Z" fill="var(--blue-dark)"/>
      <path d="M240,360 C330,330 440,320 622,316 V403 H0 V380 C80,395 170,385 240,360 Z" fill="var(--blue)"/>
    </svg>
    <div class="brand">
      <div class="brand__mark"></div>
      <div class="brand__name">MORVEN ASHCROFT</div>
      <div class="brand__sub">LAW, PLLC</div>
    </div>
    <h1 class="headline">Special Needs Planning<br>&amp; Special Needs Trusts</h1>
    <p class="offer">Use this card for a<br><strong>FREE CONSULTATION</strong></p>
    <div class="service">
      <div class="service__title">Revocable Trust</div>
      <div class="service__url">www.morvenashcroftlaw.com</div>
    </div>
  </section>

  <section class="card card--back">
    <svg class="art" width="621" height="403" viewBox="0 0 621 403" aria-hidden="true">
      <defs>
        <linearGradient id="swoosh2" x1="0" x2="1">
          <stop offset="0" stop-color="#2a2d45"/>
          <stop offset=".45" stop-color="#9d9fa6"/>
          <stop offset="1" stop-color="#ffffff"/>
        </linearGradient>
      </defs>
      <path d="M0,294 C90,262 200,250 300,256 C420,264 500,300 540,345" fill="none" stroke="url(#swoosh2)" stroke-width="5"/>
    </svg>
    <p class="tagline">Serving clients with compassion and legal<br>guidance is our passion...</p>
    <div class="headshot" role="img" aria-label="Headshot of the firm's attorney"></div>
    <div class="bio">
      <h2 class="bio__name">Morven Ashcroft Law, PLLC</h2>
      <p class="bio__text">serving client in estate planning, estate administration, probate law, wills, revocable trusts, irrevocable trusts, power of attorney, health care powers of attorney, living wills, hippa releases, guardianships, special needs planning, wealth transfers, elder law and business law in North Carolina and South Carolina.</p>
    </div>
    <div class="signature" role="img" aria-label="Attorney's handwritten signature"></div>
    <div class="brand">
      <div class="brand__mark"></div>
      <div class="brand__name">MORVEN ASHCROFT</div>
      <div class="brand__sub">LAW, PLLC</div>
    </div>
    <div class="url">www.morvenashcroftlaw.com</div>
    <address class="offices" style="font-style:normal">
      <div class="office">
        <div class="office__name">Morven Ashcroft Law, PLLC</div>
        Kerrington. 13480 Oakridge Lane, Suite 300<br>Charlotte, NC 28269
      </div>
      <div class="office">
        <div class="office__name">Morven Ashcroft Law, PLLC</div>
        Westgate Towers. 4100 Birchmont Road, Suite 1500<br>Charlotte, NC 28214
      </div>
      <div class="contact">
        <svg width="11" height="10" viewBox="0 0 11 10" aria-hidden="true"><path d="M1,4 a4,3 0 1,1 3,3 l-2,2 l0.5,-2.5 a4,3 0 0,1 -1.5,-2.5z" fill="none" stroke="var(--navy)" stroke-width="1"/></svg>
        (704) 555-0187
      </div>
      <div class="contact">
        <svg width="11" height="9" viewBox="0 0 11 9" aria-hidden="true"><rect x=".5" y=".5" width="10" height="8" fill="none" stroke="var(--navy)"/><path d="M.5,.5 L5.5,5 L10.5,.5" fill="none" stroke="var(--navy)"/></svg>
        morven@morvenashcroftlaw.com
      </div>
    </address>
  </section>

</main>
</body>
</html>
```